design a construction company business card

Design business card around our logo. Card must have all the typical info: name, title, address, phone, email, business name, etc. Somewhere on the card I would like to see our motto "Built on integrity... Inspired by commitment." Consider adding a splash of bright orange to the card to complement the blues and silvers/grays in the logo. We are open to metallic inks, textures, etc. We would like to see options on both light and dark backgrounds. The font in the logo is Euro Technic Extended Regular.

```html
<!DOCTYPE html>
<html lang="en">
<head>
<meta charset="utf-8">
<title>Harlow Contracting, Inc. — Business Card</title>
<link href="https://fonts.googleapis.com/css2?family=Michroma&family=Varela+Round&display=swap" rel="stylesheet">
<style>
  :root {
    --backdrop: #2c3034;
    --card: #ffffff;
    --brand-blue: #2b55b4;
    --rule-blue: #3b63c0;
    --rule-grey: #9a9a9a;
    --ink: #4a4a4a;
  }
  * { margin: 0; padding: 0; box-sizing: border-box; }
  html, body {
    width: 1200px;
    height: 1141px;
    overflow: hidden;
    background: var(--backdrop);
  }
  .card {
    position: absolute;
    left: 232px;
    width: 730px;
    height: 416px;
    background: var(--card);
    box-shadow: 0 4px 10px rgba(0,0,0,0.35);
  }
  .card--front { top: 120px; }
  .card--back { top: 570px; height: 412px; }

  .wordmark {
    position: absolute;
    font-family: "Michroma", sans-serif;
    color: var(--brand-blue);
    text-align: center;
    line-height: 1;
  }
  .wordmark__name { display: block; font-size: 40px; letter-spacing: 1px; }
  .wordmark__sub { display: block; font-size: 13.5px; letter-spacing: 1.5px; margin-top: 12px; }
  .card--front .wordmark { left: 42px; top: 218px; width: 268px; }
  .card--back .wordmark { left: 0; top: 190px; width: 730px; }

  .rule { position: absolute; height: 2px; top: 206px; }
  .rule--stub-left { left: 0; width: 28px; background: #b5b5b5; }
  .rule--stub-right { right: 0; width: 30px; background: #b5b5b5; }
  .rule--main { left: 328px; width: 359px; background: var(--rule-blue); }

  .contact {
    position: absolute;
    right: 43px;
    text-align: right;
    font-family: "Varela Round", sans-serif;
    color: var(--ink);
  }
  .contact__name {
    position: absolute;
    right: 43px;
    top: 146px;
    font-family: "Michroma", sans-serif;
    font-size: 28px;
    font-weight: 700;
    color: var(--brand-blue);
    letter-spacing: 0.5px;
    white-space: nowrap;
    -webkit-text-stroke: 0.6px var(--brand-blue);
  }
  .contact__title { top: 182px; font-size: 17px; }
  .contact__address { top: 214px; font-size: 17px; line-height: 22px; }
  .contact__lines { top: 282px; font-size: 17px; line-height: 24.5px; }

  .back-web {
    position: absolute;
    left: 0;
    width: 730px;
    top: 354px;
    text-align: center;
    font-family: "Varela Round", sans-serif;
    font-size: 16px;
    color: var(--ink);
  }
</style>
</head>
<body>
  <section class="card card--front">
    <span class="rule rule--stub-left"></span>
    <span class="rule rule--main"></span>
    <span class="rule rule--stub-right"></span>

    <div class="wordmark">
      <span class="wordmark__name">HARLOW</span>
      <span class="wordmark__sub">CONTRACTING, INC.</span>
    </div>

    <h1 class="contact__name">CALDER REEVES</h1>
    <p class="contact contact__title">General Manager</p>
    <p class="contact contact__address">418 W Linden St<br>Fairview, Ohio 45390</p>
    <p class="contact contact__lines">
      000-000-0000<br>
      000-000-0000<br>
      office@harlowcontracting.com<br>
      www.harlowcontracting.com
    </p>
  </section>

  <section class="card card--back">
    <div class="wordmark">
      <span class="wordmark__name">HARLOW</span>
      <span class="wordmark__sub">CONTRACTING, INC.</span>
    </div>
    <p class="back-web">www.harlowcontracting.com</p>
  </section>
</body>
</html>
```